Marketing firm Studio 847
Business card and stationery
Project: Marketing firm Studio 847
Marketing firm Studio 847  -
Creative Brief
Professional
Martin Kovalenko
Marketer, Business Strategist
Derveni, 14, 2385, Strovolia Nicosia Cyprus
Martin@studio-847.com
Www.studio-847.com
I need the logo and the dog on both, business cards and stationery. I need embossed logo or dog but I am also open to other designs.
He logo and the dog but I am also open to new design

```html
<!DOCTYPE html>
<html lang="en">
<head>
<meta charset="utf-8">
<title>Studio 847 – Business Card</title>
<link rel="stylesheet" href="https://fonts.googleapis.com/css2?family=Open+Sans:wght@400;700;800&family=Tinos&display=swap">
<style>
  :root {
    --backdrop: #2b2b2d;
    --card: #ffffff;
    --ink: #2a2a2a;
    --muted: #555555;
    --brand-purple: #8d4a9b;
    --brand-purple-light: #b487c0;
    --band-text: #ffffff;
    --band-subtext: #f1e4f4;
  }
  * { box-sizing: border-box; margin: 0; padding: 0; }
  html, body {
    width: 1200px;
    height: 780px;
    overflow: hidden;
    background: var(--backdrop);
  }
  .canvas {
    position: relative;
    width: 1200px;
    height: 780px;
  }
  .card {
    position: absolute;
    left: 100px;
    top: 90px;
    width: 1000px;
    height: 600px;
    background: var(--card);
    border-radius: 36px;
    overflow: hidden;
  }
  .brand-name {
    position: absolute;
    top: 105px;
    left: 0;
    width: 100%;
    text-align: center;
    font-family: "Open Sans", sans-serif;
    font-weight: 800;
    font-size: 112px;
    letter-spacing: 4px;
    line-height: 1;
    color: var(--ink);
    text-transform: uppercase;
  }
  .identity-band {
    position: absolute;
    left: 0;
    top: 290px;
    width: 100%;
    height: 80px;
    background: var(--brand-purple);
    border-top: 6px solid var(--brand-purple-light);
    border-bottom: 6px solid var(--brand-purple-light);
    display: flex;
    align-items: center;
    padding-left: 160px;
    font-family: "Open Sans", sans-serif;
  }
  .person-name {
    font-weight: 700;
    font-size: 32px;
    color: var(--band-text);
  }
  .band-divider {
    width: 3px;
    height: 40px;
    background: var(--band-text);
    margin: 0 26px;
  }
  .person-role {
    font-weight: 400;
    font-size: 24px;
    color: var(--band-subtext);
  }
  .contact {
    position: absolute;
    top: 405px;
    left: 0;
    width: 100%;
    font-family: "Tinos", serif;
    font-size: 27px;
    color: var(--muted);
    line-height: 42px;
  }
  .contact-line { display: block; }
  .contact-address { padding-left: 290px; }
  .contact-numbers { padding-left: 250px; }
  .contact-web { padding-left: 310px; }
  .contact-label { color: var(--brand-purple); margin-right: 6px; }
  .contact-gap { display: inline-block; width: 16px; }
</style>
</head>
<body>
  <main class="canvas">
    <section class="card" aria-label="Studio 847 business card">
      <div class="brand-name">Studio 847</div>

      <div class="identity-band">
        <span class="person-name">Martin Kovalenko</span>
        <span class="band-divider" aria-hidden="true"></span>
        <span class="person-role">Marketer, Business Strategist</span>
      </div>

      <address class="contact">
        <span class="contact-line contact-address">Derveni, 14, 2385, Strovolia Nicosia Cyprus</span>
        <span class="contact-line contact-numbers"><span class="contact-label">P:</span>22 418305<span class="contact-gap"></span><span class="contact-label">C:</span>00357 96207153<span class="contact-gap"></span><span class="contact-label">E:</span>Martin@studio-847.com</span>
        <span class="contact-line contact-web"><span class="contact-label">W:</span>Www.studio-847.com</span>
      </address>
    </section>
  </main>
</body>
</html>
```